Graphic design for an existing cardboard Archive box

We need a graphic design for an existing archive box packaging.
Our request is really simple: we would like to have a graphic design that is pleasant to put in the office or on the bookshelf in the living room.
The project must be in CMYK color space, no other colors (Pantone, spot colors, metallic inks, ecc) or varnishes can be used.
You can see and download some sample pictures and the complete flat template in Adobe Illustrator, EPS, and PDF file.

Target Market(s)

Both individual customers and professional

Industry/Entity Type

Graphic Design

Requirements
Must have
• REALLY IMPORTANT: we'd like to see 2 files: "flat graphic" on the template and applied on the 3D. Thank you

Graphic design that is pleasant to put in the office or on the bookshelf in the living room.

CMYK color space only.

We like colorful images, positive and tempting graphics.

```html
<!DOCTYPE html>
<html lang="en">
<head>
<meta charset="utf-8">
<title>Archive Box – Flat Template</title>
<link href="https://fonts.googleapis.com/css2?family=Roboto+Slab:wght@400;700&display=swap" rel="stylesheet">
<style>
  :root {
    --page: #111011;
    --stock: #141213;
    --art-base: #161416;
    --tone-cyan: #1fb8e0;
    --tone-purple: #7a5cc8;
    --tone-orange: #f7891e;
    --tone-lime: #b6d334;
    --tone-pink: #e8558f;
    --tone-grey: #3a3a3c;
    --cut: #12a53c;
    --fold: #e0262b;
    --window-frame: #8a8a8a;
    --window: #ffffff;
    --ink: #ffffff;
  }
  html, body {
    margin: 0;
    padding: 0;
    width: 1200px;
    height: 919px;
    overflow: hidden;
    background: var(--page);
  }
  .template {
    position: relative;
    width: 1200px;
    height: 919px;
  }
  .template__dieline {
    position: absolute;
    inset: 0;
    display: block;
  }
  .logo-area {
    position: absolute;
    right: 127px;
    top: 291px;
    margin: 0;
    text-align: right;
    color: var(--ink);
    font-family: "Roboto Slab", Georgia, serif;
    font-size: 27px;
    line-height: 25px;
  }
  .logo-area__line { display: block; white-space: nowrap; }
  .logo-area__line--light { font-weight: 400; }
  .logo-area__line--strong { font-weight: 700; }
</style>
</head>
<body>
<main class="template">
  <svg class="template__dieline" viewBox="0 0 1450 1111" width="1200" height="919">
    <defs>
      <clipPath id="box-shape">
        <path d="M272 20 H761 Q773 20 773 32 V112 H900 Q915 112 915 127 V246 H1345 Q1357 246 1357 258 V443 H1415 Q1430 443 1430 458 V657 Q1430 672 1415 672 H1357 V868 H915 V985 Q915 1000 900 1000 H773 V1083 Q773 1095 761 1095 H272 Q260 1095 260 1083 V1034 Q260 1022 272 1022 H315 V868 H188 V862 H70 Q55 862 55 847 V268 Q55 253 70 253 H188 V246 H315 V92 H272 Q260 92 260 80 V32 Q260 20 272 20 Z"/>
      </clipPath>
      <radialGradient id="glow-cyan-main" gradientUnits="userSpaceOnUse" cx="585" cy="745" r="120">
        <stop offset="0" stop-color="var(--tone-cyan)" stop-opacity="0.85"/>
        <stop offset="1" stop-color="var(--tone-cyan)" stop-opacity="0"/>
      </radialGradient>
      <radialGradient id="glow-lime-left" gradientUnits="userSpaceOnUse" cx="490" cy="630" r="80">
        <stop offset="0" stop-color="var(--tone-lime)" stop-opacity="0.8"/>
        <stop offset="1" stop-color="var(--tone-lime)" stop-opacity="0"/>
      </radialGradient>
      <radialGradient id="glow-purple-mid" gradientUnits="userSpaceOnUse" cx="690" cy="515" r="70">
        <stop offset="0" stop-color="var(--tone-purple)" stop-opacity="0.8"/>
        <stop offset="1" stop-color="var(--tone-purple)" stop-opacity="0"/>
      </radialGradient>
      <radialGradient id="glow-cyan-right" gradientUnits="userSpaceOnUse" cx="1075" cy="510" r="90">
        <stop offset="0" stop-color="var(--tone-cyan)" stop-opacity="0.8"/>
        <stop offset="1" stop-color="var(--tone-cyan)" stop-opacity="0"/>
      </radialGradient>
      <radialGradient id="glow-orange-right" gradientUnits="userSpaceOnUse" cx="1185" cy="620" r="80">
        <stop offset="0" stop-color="var(--tone-orange)" stop-opacity="0.85"/>
        <stop offset="1" stop-color="var(--tone-orange)" stop-opacity="0"/>
      </radialGradient>
      <radialGradient id="glow-pink-pile" gradientUnits="userSpaceOnUse" cx="1270" cy="790" r="110">
        <stop offset="0" stop-color="var(--tone-pink)" stop-opacity="0.85"/>
        <stop offset="1" stop-color="var(--tone-pink)" stop-opacity="0"/>
      </radialGradient>
      <radialGradient id="glow-lime-window" gradientUnits="userSpaceOnUse" cx="945" cy="745" r="75">
        <stop offset="0" stop-color="var(--tone-lime)" stop-opacity="0.75"/>
        <stop offset="1" stop-color="var(--tone-lime)" stop-opacity="0"/>
      </radialGradient>
      <radialGradient id="glow-cyan-side" gradientUnits="userSpaceOnUse" cx="272" cy="435" r="55">
        <stop offset="0" stop-color="var(--tone-cyan)" stop-opacity="0.7"/>
        <stop offset="1" stop-color="var(--tone-cyan)" stop-opacity="0"/>
      </radialGradient>
      <radialGradient id="glow-top-lid" gradientUnits="userSpaceOnUse" cx="530" cy="205" r="110">
        <stop offset="0" stop-color="var(--tone-cyan)" stop-opacity="0.5"/>
        <stop offset="0.5" stop-color="var(--tone-purple)" stop-opacity="0.3"/>
        <stop offset="1" stop-color="var(--tone-orange)" stop-opacity="0"/>
      </radialGradient>
      <radialGradient id="glow-grey-cloud" gradientUnits="userSpaceOnUse" cx="600" cy="560" r="520">
        <stop offset="0" stop-color="var(--tone-grey)" stop-opacity="0.7"/>
        <stop offset="1" stop-color="var(--tone-grey)" stop-opacity="0"/>
      </radialGradient>
      <linearGradient id="glow-bottom-pile" x1="0" y1="0" x2="0" y2="1">
        <stop offset="0" stop-color="var(--tone-orange)" stop-opacity="0"/>
        <stop offset="0.6" stop-color="var(--tone-purple)" stop-opacity="0.35"/>
        <stop offset="1" stop-color="var(--tone-pink)" stop-opacity="0.6"/>
      </linearGradient>
    </defs>

    <path class="box-stock" d="M272 20 H761 Q773 20 773 32 V112 H900 Q915 112 915 127 V246 H1345 Q1357 246 1357 258 V443 H1415 Q1430 443 1430 458 V657 Q1430 672 1415 672 H1357 V868 H915 V985 Q915 1000 900 1000 H773 V1083 Q773 1095 761 1095 H272 Q260 1095 260 1083 V1034 Q260 1022 272 1022 H315 V868 H188 V862 H70 Q55 862 55 847 V268 Q55 253 70 253 H188 V246 H315 V92 H272 Q260 92 260 80 V32 Q260 20 272 20 Z" fill="var(--stock)"/>

    <g class="artwork" clip-path="url(#box-shape)" role="img" aria-label="Colourful 3D jigsaw puzzle pieces in cyan, purple, orange, lime and pink scattered over faint grey puzzle pieces, piling up along the bottom edge">
      <rect x="55" y="118" width="1302" height="877" fill="var(--art-base)"/>
      <rect x="55" y="118" width="1302" height="877" fill="url(#glow-grey-cloud)"/>
      <rect x="315" y="118" width="452" height="135" fill="url(#glow-top-lid)"/>
      <rect x="55" y="118" width="1302" height="877" fill="url(#glow-cyan-side)"/>
      <rect x="55" y="118" width="1302" height="877" fill="url(#glow-purple-mid)"/>
      <rect x="55" y="118" width="1302" height="877" fill="url(#glow-lime-left)"/>
      <rect x="55" y="118" width="1302" height="877" fill="url(#glow-cyan-main)"/>
      <rect x="55" y="118" width="1302" height="877" fill="url(#glow-cyan-right)"/>
      <rect x="55" y="118" width="1302" height="877" fill="url(#glow-orange-right)"/>
      <rect x="55" y="118" width="1302" height="877" fill="url(#glow-lime-window)"/>
      <rect x="55" y="118" width="1302" height="877" fill="url(#glow-pink-pile)"/>
      <rect x="188" y="790" width="1169" height="78" fill="url(#glow-bottom-pile)"/>
    </g>

    <g class="fold-lines" stroke="var(--fold)" stroke-width="1.6" stroke-dasharray="3 3" fill="none">
      <line x1="327" y1="30" x2="327" y2="90"/>
      <line x1="327" y1="1030" x2="327" y2="1088"/>
      <line x1="322" y1="118" x2="767" y2="118"/>
      <line x1="322" y1="253" x2="767" y2="253"/>
      <line x1="322" y1="862" x2="767" y2="862"/>
      <line x1="322" y1="995" x2="767" y2="995"/>
      <line x1="322" y1="253" x2="322" y2="862"/>
      <line x1="767" y1="118" x2="767" y2="995"/>
      <line x1="907" y1="253" x2="907" y2="862"/>
      <line x1="193" y1="258" x2="193" y2="862"/>
      <line x1="1347" y1="258" x2="1347" y2="862"/>
    </g>

    <g class="windows">
      <rect x="783" y="285" width="106" height="168" rx="8" fill="var(--window-frame)"/>
      <rect x="790" y="292" width="92" height="154" rx="4" fill="var(--window)"/>
      <rect x="783" y="609" width="106" height="168" rx="8" fill="var(--window-frame)"/>
      <rect x="790" y="616" width="92" height="154" rx="4" fill="var(--window)"/>
    </g>

    <g class="finger-holes" stroke="var(--cut)" stroke-width="2.5" fill="none">
      <circle cx="194" cy="558" r="17"/>
      <circle cx="767" cy="558" r="18"/>
      <circle cx="907" cy="558" r="18"/>
      <path d="M1357 540 A18 18 0 0 1 1357 576"/>
    </g>

    <path class="cut-line" d="M272 20 H761 Q773 20 773 32 V112 H900 Q915 112 915 127 V246 H1345 Q1357 246 1357 258 V443 H1415 Q1430 443 1430 458 V657 Q1430 672 1415 672 H1357 V868 H915 V985 Q915 1000 900 1000 H773 V1083 Q773 1095 761 1095 H272 Q260 1095 260 1083 V1034 Q260 1022 272 1022 H315 V868 H188 V862 H70 Q55 862 55 847 V268 Q55 253 70 253 H188 V246 H315 V92 H272 Q260 92 260 80 V32 Q260 20 272 20 Z" fill="none" stroke="var(--cut)" stroke-width="2.5"/>
  </svg>

  <p class="logo-area">
    <span class="logo-area__line logo-area__line--light">put your</span>
    <span class="logo-area__line logo-area__line--strong">logo area</span>
  </p>
</main>
</body>
</html>
```